Media/PR business needs a website upgrade

Modernise my website www.vrl.net.au into a simpler and mobile friendly site with the usual plugins, maximum 5 pages, 4 might be enough. My page is already hosted and I have an email address so I just want to work with a designer who is fantastic with WordPress, to refresh and simplify the 6 year-old look.

Target Market(s)

men & women 25-55

Industry/Entity Type

Business

Coding

Coded - Design and coding required

Number of Pages Required

4 page

Font styles to use
Sans Serif

Colors
f37122
ffffff

Requirements
Must have
• Social media plugins, about, client portfolio, contact (can be under about)blog capability
Nice to have
• photos of jobs I've done
Should not have
• e-commerce, can lose all the client logos

```html
<!DOCTYPE html>
<html lang="en">
<head>
<meta charset="utf-8">
<title>Vista Reach Links – About</title>
<link rel="stylesheet" href="https://fonts.googleapis.com/css2?family=Questrial&family=Open+Sans:wght@300;400;600&display=swap">
<style>
:root{
  --orange:#f37122;
  --button:#f7941d;
  --white:#ffffff;
  --panel:#f0f3f5;
  --ink:#333333;
  --text:#444444;
  --footer:#464646;
  --footer-bar:#373737;
  --divider:#e3e3e3;
  --muted:#9a9a9a;
}
*{box-sizing:border-box;margin:0;padding:0}
html,body{width:1200px;height:1182px;overflow:hidden;background:var(--white)}
body{position:relative;font-family:"Open Sans",sans-serif;color:var(--text)}
.about{position:absolute;left:0;top:58px;width:1200px;height:554px;background:var(--panel)}
.section-title{position:absolute;left:0;width:1200px;text-align:center;font-family:"Questrial",sans-serif;font-weight:400}
.about-title{top:42px;font-size:27px;color:var(--orange)}
.about-lead{top:86px;font-size:24px;color:var(--ink)}
.about-text{position:absolute;left:140px;width:920px;text-align:center;font-size:11.6px;font-weight:300;line-height:22px;color:var(--ink)}
.pillar{position:absolute;top:296px;width:280px;text-align:center}
.pillar svg{display:block;margin:0 auto;height:50px}
.pillar h3{margin-top:16px;font-size:13.5px;font-weight:600;color:var(--ink);letter-spacing:.2px}
.pillar p{margin-top:16px;font-size:11.6px;font-weight:300;line-height:18.5px;color:var(--ink)}
.btn{position:absolute;left:536px;top:475px;width:127px;height:40px;background:var(--button);color:var(--white);font-size:11px;font-weight:600;letter-spacing:.3px;display:flex;align-items:center;justify-content:center;text-decoration:none}
.portfolio-title{top:668px;font-size:26px;color:var(--ink)}
.clients{position:absolute;left:170px;top:732px;width:880px;height:93px;display:flex}
.client{display:flex;align-items:center;justify-content:center;gap:6px;font-family:"Open Sans",sans-serif;font-size:13px;font-weight:600;color:var(--ink);border-right:1px solid var(--divider)}
.client:last-child{border-right:none}
.client .mark{width:10px;height:10px;border-radius:50%;background:var(--orange)}
.footer{position:absolute;left:0;top:868px;width:1200px;height:314px;background:var(--footer);color:var(--white)}
.brand{position:absolute;left:143px;top:28px;display:flex;align-items:center;gap:10px}
.brand .mark{width:56px;height:56px;border-radius:50%;background:var(--orange)}
.brand span{font-family:"Questrial",sans-serif;font-size:17px;line-height:16px;color:var(--white)}
.social{position:absolute;left:212px;top:113px;display:flex;gap:16px}
.social span{width:13px;height:13px;border-radius:50%;background:var(--muted)}
.links{position:absolute;top:36px;list-style:none;font-size:10.5px}
.links li{height:24px}
.links a{color:var(--white);text-decoration:none}
.contact{position:absolute;left:753px;top:37px;font-size:10.5px;line-height:19.3px}
.contact .org{margin-bottom:6px}
.contact b{font-weight:400;display:inline-block;margin-right:8px;padding-left:1px}
.bar{position:absolute;left:130px;top:246px;width:940px;height:68px;background:var(--footer-bar);font-size:10.5px}
.bar .copy{position:absolute;left:27px;top:29px}
.bar .legal{position:absolute;right:32px;top:29px;display:flex;gap:12px}
.bar a{color:var(--white);text-decoration:none}
</style>
</head>
<body>
<section class="about">
  <h2 class="section-title about-title">About Us</h2>
  <h1 class="section-title about-lead">Maya grew up on Scotland Island in Pittwater on Sydney’s northern</h1>
  <p class="about-text" style="top:124px">Maya grew up on Scotland Island in Pittwater on Sydney’s northern beaches, the breeding ground for many Australian sailing greats including the Harlows, Penrys and the Carvers.</p>
  <p class="about-text" style="top:169px">As a ‘tinny terror’ she attended Kellet Bay Public School then Northshore Ridge High School with some of these sailing families, and now through her work she’s back mingling with the greats.</p>
  <p class="about-text" style="top:214px">A communications degree at the Capital Plains University, a career that has seen her rise to the top of her specialist field and three children later has brought her full circle back to the island as a home owner.</p>

  <div class="pillar" style="left:147px">
    <svg viewBox="0 0 64 50" fill="none" stroke="#333" stroke-width="2"><path d="M2 32 Q32 4 62 32 Q32 60 2 32Z"/><circle cx="32" cy="32" r="9"/><circle cx="32" cy="32" r="3" fill="#333"/><path d="M32 2v8M14 8l4 7M50 8l-4 7M4 16l6 5M60 16l-6 5"/></svg>
    <h3>OUR VISION</h3>
    <p>Being a thoughtful mother &amp; partner, running a successful business and being a good friend maintain Maya’s busy and well-rounded life.</p>
  </div>
  <div class="pillar" style="left:461px">
    <svg viewBox="0 0 64 50" fill="none" stroke="#333" stroke-width="2"><path d="M10 46 L32 18 L54 46Z"/><path d="M32 18V4h10v7H32"/><path d="M14 41l9-6 6 4 8-7"/></svg>
    <h3>OUR MISSION</h3>
    <p>Being a thoughtful mother &amp; partner, running a successful business and being a good friend maintain Maya’s busy and well-rounded life.</p>
  </div>
  <div class="pillar" style="left:772px">
    <svg viewBox="0 0 64 50" fill="none" stroke="#333" stroke-width="2"><rect x="15" y="4" width="34" height="44" rx="3"/><rect x="25" y="1" width="14" height="6" rx="1"/><path d="M21 22h5l3-5 4 9 3-5h7M21 34h22M21 40h14"/></svg>
    <h3>OUR EXPERIENCE</h3>
    <p>Being a thoughtful mother &amp; partner, running a successful business and being a good friend maintain Maya’s busy and well-rounded life.</p>
  </div>
  <a class="btn" href="#">LEARN MORE</a>
</section>

<h2 class="section-title portfolio-title">Client Portfolio</h2>
<div class="clients">
  <div class="client" style="width:123px"><span class="mark"></span>Keelworks</div>
  <div class="client" style="width:151px"><span class="mark"></span>Harbour Cup</div>
  <div class="client" style="width:155px"><span class="mark"></span>Bluewater Club</div>
  <div class="client" style="width:149px"><span class="mark"></span>Shoreguard</div>
  <div class="client" style="width:154px"><span class="mark"></span>Tidemark</div>
  <div class="client" style="width:148px"><span class="mark"></span>Coastline Council</div>
</div>

<footer class="footer">
  <div class="brand"><span class="mark"></span><span>Vista<br>Reach<br>Links</span></div>
  <div class="social" aria-label="Social media links"><span></span><span></span><span></span><span></span></div>
  <ul class="links" style="left:408px">
    <li><a href="#">Home</a></li><li><a href="#">Services</a></li><li><a href="#">About</a></li><li><a href="#">Client Portfolio</a></li><li><a href="#">Testimonials</a></li><li><a href="#">Blog</a></li><li><a href="#">Contact</a></li>
  </ul>
  <ul class="links" style="left:556px">
    <li><a href="#">Sports media</a></li><li><a href="#">Publicity</a></li><li><a href="#">Sponsorship leverage</a></li><li><a href="#">Event management</a></li><li><a href="#">Crisis management</a></li><li><a href="#">Social media</a></li><li><a href="#">Writing &amp; editing web</a></li><li><a href="#">Storytelling</a></li>
  </ul>
  <div class="contact">
    <div class="org">Vista Reach Links</div>
    <div><b>Phone:</b>+61 400 555 012</div>
    <div><b>Address:</b>PO Box 2040, Reef Point NSW 2999 Australia</div>
    <div><b>Email:</b>maya@vrl.net.au</div>
    <div><b>ABN:</b>12 345 678 901</div>
  </div>
  <div class="bar">
    <span class="copy">Copyright 2017 All Rights Reserved by Vista Reach Links</span>
    <span class="legal"><a href="#">Terms &amp; Conditions</a><a href="#">Privacy Policy</a></span>
  </div>
</footer>
</body>
</html>
```